Calder Mindworks Psychology website transfer from WIX to Wordpress

I have a website currently coded in WIX and I want it (or something like it or better) designed to be coded on Wordpress instead. The website should have mobile optimization so that it can be viewed on mobile devices.

The current website is at: www.caldermindworks.example

I'm not looking for versions of the website that are very different to what I already have, unless they improve on it aesthetically. I'm mainly looking to have a Wordpress version of this website that I built, away from the WIX ecosystem.

Target Market(s)

Psychology services clients

Coding

Coded - Design and coding required

Number of Pages Required

5+ page

Font styles to use
Serif

Requirements
Must have
• The finished product shoud match my website exactly.
Nice to have
• I'm happy to see new ideas that improve on the current website.
Should not have
• It should not be a different version of my website.

```html
<!DOCTYPE html>
<html lang="en">
<head>
<meta charset="utf-8">
<title>Calder Mindworks Psychology</title>
<link rel="stylesheet" href="https://fonts.googleapis.com/css2?family=Figtree:wght@400;500;600&family=Mrs+Saint+Delafield&display=swap">
<style>
:root{
  --green:#2f5a4d;
  --green-dark:#284d42;
  --ink:#2d2d2d;
  --muted:#5a5a5a;
  --beige:#ede7e0;
  --white:#ffffff;
  --script:"Mrs Saint Delafield", cursive;
  --sans:"Figtree", sans-serif;
}
*{box-sizing:border-box;margin:0;padding:0}
html,body{width:1200px;height:3942px;overflow:hidden}
body{font-family:var(--sans);color:var(--ink);background:var(--white);position:relative}
.abs{position:absolute}
.btn{position:absolute;display:flex;align-items:center;justify-content:center;border:2px solid var(--green);border-radius:40px;color:var(--green);font-size:15px;font-weight:500}

/* header */
.site-header{position:absolute;left:0;top:0;width:1200px;height:80px;background:var(--green)}
.brand{position:absolute;display:flex;align-items:center;gap:10px;color:var(--white);font-size:20px;font-weight:500;letter-spacing:.5px}
.brand .dot{width:14px;height:14px;border-radius:50%;border:2px solid var(--white)}
.site-header .brand{left:142px;top:26px}
.nav a{position:absolute;top:30px;color:var(--white);font-size:14px;text-decoration:none}
.quote-btn{left:932px;top:18px;width:124px;height:39px;border-color:var(--white);color:var(--white);font-size:14px;font-weight:600}

/* hero */
.hero{position:absolute;left:0;top:80px;width:1200px;height:480px;background:radial-gradient(ellipse at 50% 65%,#5d7268 0%,#3b4742 40%,#2c302e 100%)}
.hero-title{position:absolute;left:0;top:40px;width:1200px;text-align:center;font-family:var(--script);color:var(--white);font-size:230px;line-height:1}
.hero-rule{position:absolute;left:450px;top:268px;width:490px;height:2px;background:var(--white)}
.hero-sub{position:absolute;left:0;top:288px;width:1200px;text-align:center;color:var(--white);font-size:50px;letter-spacing:1px}

/* about */
.portrait-frame{left:173px;top:653px;width:347px;height:536px;border:1.5px solid #777;border-radius:174px}
.portrait{left:182px;top:653px;width:330px;height:510px;border-radius:165px;background:linear-gradient(160deg,#d9d3cc 0%,#a96a55 45%,#57534f 100%)}
.about-text{left:578px;top:690px;width:448px;text-align:center}
.about-text .name{font-family:var(--script);font-size:52px;color:var(--green);line-height:1}
.about-text h2{font-size:20px;font-weight:400;line-height:28px;margin-top:6px}
.about-text p{font-size:12.5px;line-height:20px;color:var(--muted);margin-top:20px;text-align:justify;text-align-last:center}
.learn-btn{left:741px;top:1123px;width:122px;height:39px}

/* services grid */
.section-script{font-family:var(--script);color:var(--ink);line-height:1;white-space:nowrap}
.services-title{left:142px;top:1308px;font-size:80px}
.services-btn{left:881px;top:1330px;width:172px;height:38px}
.tile{width:399px;height:299px}
.tile-label{width:400px;text-align:center;color:var(--green);font-size:15.5px;font-weight:500}

/* psychosexual */
.beige{left:0;top:2138px;width:1200px;height:575px;background:var(--beige)}
.what-title{left:142px;top:2248px;font-size:64px;line-height:64px}
.what-text{left:142px;top:2408px;width:440px;font-size:13px;line-height:20px;color:var(--muted);text-align:justify}
.help-btn{left:142px;top:2543px;width:381px;height:38px;font-size:14px}
.ring{left:633px;top:2219px;width:398px;height:398px;border-radius:50%;border:2px solid var(--green)}
.ring-photo{left:651px;top:2237px;width:362px;height:362px;border-radius:50%;background:linear-gradient(150deg,#f3f2ef 0%,#cfd2d3 55%,#7d8487 100%)}

/* offers */
.offer-title{left:0;top:2800px;width:1200px;text-align:center;font-size:70px}
.card{width:279px;height:398px;border:2px solid var(--green);border-radius:140px;text-align:center;padding-top:78px}
.card svg.icon{display:block;margin:0 auto}
.card h3{font-size:21px;font-weight:500;color:var(--green);line-height:28px;margin-top:18px}
.card p{font-size:13px;line-height:20px;color:var(--muted);margin:12px auto 0;width:200px}
.card .arrow{display:block;margin:22px auto 0}

/* footer */
.site-footer{left:0;top:3424px;width:1200px;height:446px;background:var(--green);color:var(--white)}
.site-footer .brand{left:142px;top:108px}
.foot-welcome{left:142px;top:156px;width:270px;font-size:11.5px;line-height:20px;text-align:justify}
.flag{width:44px;height:28px}
.hours{left:510px;top:106px;width:250px;font-size:11.5px;line-height:20px}
.hours h4{font-size:19px;font-weight:500;margin-bottom:14px}
.hours .u{text-decoration:underline;margin-top:14px;margin-bottom:8px}
.ack{left:787px;top:104px;width:268px;font-size:11.5px;line-height:20px;text-align:justify}
.copyright{left:0;top:3870px;width:1200px;height:72px;background:var(--green-dark);color:var(--white);font-size:12px;display:flex;align-items:center;justify-content:center}
</style>
</head>
<body>

<header class="site-header">
  <div class="brand"><span class="dot"></span>Calder Mindworks Psychology</div>
  <nav class="nav">
    <a style="left:612px">Home</a>
    <a style="left:686px">FAQs</a>
    <a style="left:755px">About</a>
    <a style="left:828px">Services</a>
  </nav>
  <div class="btn quote-btn">Get A Quote</div>
</header>

<section class="hero" role="img" aria-label="Dim green-toned archway corridor photograph">
  <div class="hero-title">Calder</div>
  <div class="hero-rule"></div>
  <div class="hero-sub">MINDWORKS PSYCHOLOGY</div>
</section>

<section class="about">
  <div class="abs portrait-frame"></div>
  <div class="abs portrait" role="img" aria-label="Photo of the psychologist seated in an armchair writing on a clipboard"></div>
  <div class="abs about-text">
    <div class="name">Dr Rowan Calder</div>
    <h2>Clinical and Counselling Psychologist<br>Clinical Psychosexual Therapist</h2>
    <p>My name is Rowan (he/they) and I am a Clinical and Counselling Psychologist, and accredited Clinical Psychosexual Therapist, with over 15 years' experience working with adults and young people of all abilities and identities.</p>
    <p>My practice focuses on sex therapy and working with diversity, which regularly includes supporting members of LGBTQIA+, neurodivergent, and disabled communities. Because of this work, I am sex-positive and kink-, polyamory-, LGBTQIA+ and neurodiversity knowledgeable and affirming in my practice. I am also a member of many lived experience communities as part of my commitment to lifelong learning and honoring lived experience.</p>
    <p>I know that seeing a therapist can sometimes be anxiety-evoking, and as such, I always aim to curate a non-judgmental, collaborative, and intentional approach to working with people toward their personal goals and a life of value.</p>
  </div>
  <div class="btn learn-btn">Learn More</div>
</section>

<section class="services">
  <div class="abs section-script services-title">Our Services</div>
  <div class="btn services-btn">View More Services</div>

  <div class="abs tile" style="left:0;top:1412px;background:linear-gradient(135deg,#2f4a2e,#6b5a46 60%,#c9b9a4)" role="img" aria-label="Couple embracing in front of green foliage"></div>
  <div class="abs tile" style="left:401px;top:1412px;background:linear-gradient(135deg,#e8e4df,#b38c74 55%,#5b4438)" role="img" aria-label="Couple lying close together on white sheets"></div>
  <div class="abs tile" style="left:801px;top:1412px;background:linear-gradient(135deg,#9a8a7a,#7c3a2c 55%,#3c3430)" role="img" aria-label="Two friends standing on a city street"></div>
  <div class="abs tile-label" style="left:0;top:1732px">Neurodivergence &amp; Disability</div>
  <div class="abs tile-label" style="left:400px;top:1732px">Intimacy &amp; Connection</div>
  <div class="abs tile-label" style="left:800px;top:1732px">Gender Identity &amp; Affirmation</div>

  <div class="abs tile" style="left:0;top:1772px;background:linear-gradient(135deg,#c8d0a8,#5d7a4a 50%,#3d5a78)" role="img" aria-label="Couple outdoors, one pointing into the distance"></div>
  <div class="abs tile" style="left:401px;top:1772px;background:linear-gradient(135deg,#efede8,#c9b24e 45%,#4a4440)" role="img" aria-label="Two men laughing together on a sofa"></div>
  <div class="abs tile" style="left:801px;top:1772px;background:linear-gradient(135deg,#e4dcd4,#a7735e 55%,#4a3129)" role="img" aria-label="Couple resting heads together in bed"></div>
  <div class="abs tile-label" style="left:0;top:2092px">Sexual &amp; Interpersonal Trauma</div>
  <div class="abs tile-label" style="left:400px;top:2092px">Mismatched Libido &amp; Sex 'Addiction'</div>
  <div class="abs tile-label" style="left:800px;top:2092px">Sexual Identity &amp; Diversity</div>
</section>

<section class="abs beige"></section>
<div class="abs section-script what-title">What is a Clinical<br>Psychosexual Therapist?</div>
<p class="abs what-text">Sometimes referred to as a sex therapist, a Clinical Psychosexual Therapist is someone who has postgraduate university qualifications in the field of human sexuality, which is a broad area encompassing subjects like: sexual orientation, gender identity, sexual function and diversity, sexual and reproductive health, intersectional feminism, relationship dynamics, and sexual trauma.</p>
<div class="btn help-btn">How can a clinical psychosexual therapist help me?</div>
<div class="abs ring"></div>
<div class="abs ring-photo" role="img" aria-label="Therapist in a grey blazer seated in a bright office"></div>

<section class="offers">
  <div class="abs section-script offer-title">Support and services I offer:</div>

  <div class="abs card" style="left:141px;top:2900px">
    <svg class="icon" width="56" height="60" viewBox="0 0 56 60" fill="none" stroke="#2f5a4d" stroke-width="2"><path d="M14 56V44c-6-4-9-10-9-18C5 13 15 4 28 4s23 9 23 22c0 6-3 9-3 13l5 7-6 2v6c0 2-2 3-4 3h-7v4"/><circle cx="28" cy="24" r="10"/><path d="M28 14v20M18 24h20"/></svg>
    <h3>Psychological<br>Therapy</h3>
    <p>Psychological assessment, education, counselling, and therapy using person-centered and evidence-based integrative therapeutic interventions.</p>
    <svg class="arrow" width="12" height="16" viewBox="0 0 12 16" fill="none" stroke="#2d2d2d" stroke-width="2"><path d="M3 2l6 6-6 6"/></svg>
  </div>

  <div class="abs card" style="left:459px;top:2900px">
    <svg class="icon" width="64" height="60" viewBox="0 0 64 60" fill="none" stroke="#2f5a4d" stroke-width="2"><rect x="24" y="4" width="30" height="22"/><path d="M30 18l6-6 5 4 7-8"/><path d="M4 34h56M10 34v22M54 34v22"/><circle cx="14" cy="22" r="5"/><path d="M6 34c0-5 3-7 8-7s8 2 8 7"/><rect x="28" y="40" width="18" height="8"/></svg>
    <h3>Clinical<br>Supervision</h3>
    <p>Clinical supervision to support provisional psychologists and registrars, early career mentoring, technical skill building, and clinical case discussion.</p>
    <svg class="arrow" width="12" height="16" viewBox="0 0 12 16" fill="none" stroke="#2d2d2d" stroke-width="2"><path d="M3 2l6 6-6 6"/></svg>
  </div>

  <div class="abs card" style="left:777px;top:2900px">
    <svg class="icon" width="60" height="60" viewBox="0 0 60 60" fill="none" stroke="#2f5a4d" stroke-width="2"><rect x="20" y="4" width="20" height="14" rx="2"/><path d="M26 18l-2 5 6-5"/><circle cx="14" cy="28" r="5"/><circle cx="46" cy="28" r="5"/><path d="M4 44c0-6 4-9 10-9s10 3 10 9M36 44c0-6 4-9 10-9s10 3 10 9"/><path d="M4 46h52M12 46v10M48 46v10M30 34v22"/></svg>
    <h3>Training and<br>Consultancy</h3>
    <p>Training for general psychology or special interest subjects like sexology and neurodivergence, and consultancy for practices and organisations.</p>
    <svg class="arrow" width="12" height="16" viewBox="0 0 12 16" fill="none" stroke="#2d2d2d" stroke-width="2"><path d="M3 2l6 6-6 6"/></svg>
  </div>
</section>

<footer class="abs site-footer">
  <div class="brand"><span class="dot"></span>Calder Mindworks Psychology</div>
  <p class="abs foot-welcome">At Calder Mindworks Psychology, we welcome people of all backgrounds, race, ethnicity, genders, sexuality, relationship type, neurotype, and abilities. Please contact us if we can assist you to make your appointment more inclusive in any way or provide us feedback on how we can do better.</p>
  <div class="abs flag" style="left:144px;top:316px;background:linear-gradient(180deg,#d94a3a,#e6a23c,#e6d34a,#4a9a5a,#3a6ab0,#7a4a9a)" role="img" aria-label="Progress pride flag"></div>
  <div class="abs flag" style="left:200px;top:316px;background:#d9a23c" role="img" aria-label="Neurodiversity flag"></div>
  <div class="abs flag" style="left:256px;top:316px;background:linear-gradient(135deg,#3a3a3a,#8a6a5a 40%,#9ac0d0 60%,#e6b0c0)" role="img" aria-label="Disability pride flag"></div>

  <div class="abs hours">
    <h4>Practice Hours</h4>
    <div>Mondays 9:30am - 3:30pm</div>
    <div>Thursdays: 8:30am - 2:30pm</div>
    <div class="u">If you need support between appointments or after hours, please consider contacting:</div>
    <div>Harbour Line on 13 00 11</div>
    <div>Youth Talkline on 1800 000 210</div>
    <div>Brothers Talk on 1300 000 318</div>
    <div>NightCall Support on 1300 000 427</div>
    <div>Clear Mind on 1300 000 536</div>
    <div>Young Minds Hub on 1800 000 645</div>
    <div>Pride Connect on 1800 000 754</div>
    <div>Yarning Line on 13 00 86</div>
  </div>

  <p class="abs ack">We acknowledge the Traditional Custodians of the lands upon which we work here in Meanjin, the Turrbal and Jaggera peoples, as the first inhabitants of our nation. We recognise their continuing connection to land, water, and culture and pay our respects to their Elders past, present, and emerging – as well as First Nations people and the stolen generation who have yet to find their home. Their lands never ceded sovereignty. Always was, always will be, Aboriginal land.</p>
  <div class="abs flag" style="left:789px;top:316px;background:linear-gradient(180deg,#1a1a1a 50%,#c8321e 50%)" role="img" aria-label="Aboriginal flag"></div>
  <div class="abs flag" style="left:835px;top:316px;background:linear-gradient(180deg,#2f8a4a 20%,#1e3f8a 20%,#1e3f8a 80%,#2f8a4a 80%)" role="img" aria-label="Torres Strait Islander flag"></div>
</footer>

<div class="abs copyright">© Copyrights 2024 | All Rights Reserved</div>

</body>
</html>
```